Boring Fiberglass Repair Company needs creative business cards

The Fiberglass Repair industry isn't very fun or creative but we'd like a business card that communicates a fresh, modern, and service-oriented feel. We repair bathroom fixtures (bath tubs, showers, etc) which are made out of fiberglass. Our fiberglass repair service will be sold to bathtub manufacturers and also businesses that sell bathtubs. We will also offer our services to home owners that have broken showers and bathtubs.
Target Market(s)
Home builders, plumbing wholesalers, home owners
Contact Information for Business Card
Name
Phone Number
Email Address
Business Address
Tag line: "Quality Craftsmanship Today"
Look and feel

```html
<!DOCTYPE html>
<html lang="en">
<head>
<meta charset="utf-8">
<title>Northbay Fiberglass – Business Card</title>
<link href="https://fonts.googleapis.com/css2?family=Montserrat:wght@600;800&family=Roboto:wght@400&display=swap" rel="stylesheet">
<style>
  :root {
    --backdrop: #2b2b2d;
    --navy: #0d3561;
    --navy-light: #1a5283;
    --red: #e3202f;
    --white: #ffffff;
    --ink-grey: #6b6b6b;
    --rule: #333333;
  }
  * { box-sizing: border-box; margin: 0; padding: 0; }
  html, body {
    width: 1200px; height: 929px; overflow: hidden;
    background: var(--backdrop);
  }
  .sheet {
    width: 1200px; height: 929px;
    display: flex; flex-direction: column; align-items: center; justify-content: center;
    gap: 40px;
  }
  .card {
    position: relative;
    width: 680px; height: 389px;
    overflow: hidden;
    box-shadow: 0 10px 30px rgba(0,0,0,.45);
  }
  /* Front */
  .card--front {
    background: radial-gradient(ellipse at 60% 65%, var(--navy-light) 0%, var(--navy) 70%);
    color: var(--white);
    text-align: center;
  }
  .brand-name {
    font-family: "Montserrat", sans-serif;
    font-weight: 800;
    letter-spacing: 1px;
    text-transform: uppercase;
    line-height: 1;
  }
  .card--front .brand-name {
    position: absolute; left: 0; right: 0; top: 150px;
    font-size: 40px; color: var(--white);
  }
  .tagline {
    position: absolute; left: 0; right: 0; top: 262px;
    font-family: "Roboto", sans-serif; font-size: 15px; letter-spacing: 1.2px;
    color: var(--white);
  }
  /* Back */
  .card--back { background: var(--white); }
  .card--back .brand-name {
    position: absolute; left: 150px; top: 98px;
    font-size: 38px; color: var(--navy);
  }
  .holder {
    position: absolute; left: 52px; top: 245px; width: 320px;
    text-align: right;
  }
  .holder__name {
    font-family: "Montserrat", sans-serif; font-weight: 600;
    font-size: 24px; color: var(--navy); text-transform: uppercase;
  }
  .holder__title {
    font-family: "Montserrat", sans-serif; font-weight: 600;
    font-size: 15px; color: var(--red); margin-top: 2px;
  }
  .divider {
    position: absolute; left: 395px; top: 200px;
    width: 1px; height: 125px; background: var(--rule);
  }
  .contact {
    position: absolute; left: 412px; top: 198px;
    font-family: "Roboto", sans-serif; font-size: 13px; line-height: 20px;
    color: var(--ink-grey); list-style: none;
  }
  .contact__item { display: flex; align-items: center; gap: 7px; }
  .contact__item--plain { padding-left: 0; }
  .contact__icon { width: 13px; height: 13px; fill: var(--navy); flex: none; }
  .band { position: absolute; left: 0; bottom: 0; }
</style>
</head>
<body>
<main class="sheet">
  <section class="card card--front" aria-label="Card front">
    <div class="brand-name">Northbay Fiberglass</div>
    <p class="tagline">Quality Craftsmanship Today</p>
  </section>

  <section class="card card--back" aria-label="Card back">
    <div class="brand-name">Northbay Fiberglass</div>

    <div class="holder">
      <div class="holder__name">Daniel Harwick</div>
      <div class="holder__title">Managing Director</div>
    </div>

    <div class="divider"></div>

    <ul class="contact">
      <li class="contact__item contact__item--plain">48 Maple Ridge Road,</li>
      <li class="contact__item contact__item--plain">Oakvale, ON K2M 4T7</li>
      <li class="contact__item">
        <svg class="contact__icon" viewBox="0 0 24 24" aria-hidden="true"><path d="M6.6 10.8a15.1 15.1 0 0 0 6.6 6.6l2.2-2.2a1 1 0 0 1 1-.25 11.4 11.4 0 0 0 3.6.57 1 1 0 0 1 1 1V20a1 1 0 0 1-1 1A17 17 0 0 1 3 4a1 1 0 0 1 1-1h3.5a1 1 0 0 1 1 1c0 1.25.2 2.45.57 3.57a1 1 0 0 1-.25 1z"/></svg>
        +15550123488
      </li>
      <li class="contact__item">
        <svg class="contact__icon" viewBox="0 0 24 24" aria-hidden="true"><path d="M2 5h20v14H2zm2 2v.5l8 5 8-5V7zm0 2.8V17h16V9.8l-8 5z"/></svg>
        dharwick@northbayfiberglass.com
      </li>
      <li class="contact__item">
        <svg class="contact__icon" viewBox="0 0 24 24" aria-hidden="true"><path d="M12 2a10 10 0 1 0 0 20 10 10 0 0 0 0-20zm6.9 6h-2.9a15.6 15.6 0 0 0-1.4-3.6A8 8 0 0 1 18.9 8zM12 4a14 14 0 0 1 1.9 4h-3.8A14 14 0 0 1 12 4zM4.3 14a8 8 0 0 1 0-4h3.4a16 16 0 0 0 0 4zm.8 2h2.9a15.6 15.6 0 0 0 1.4 3.6A8 8 0 0 1 5.1 16zM8 8H5.1a8 8 0 0 1 4.3-3.6A15.6 15.6 0 0 0 8 8zm4 12a14 14 0 0 1-1.9-4h3.8A14 14 0 0 1 12 20zm2.3-6H9.7a14.7 14.7 0 0 1 0-4h4.6a14.7 14.7 0 0 1 0 4zm.3 5.6a15.6 15.6 0 0 0 1.4-3.6h2.9a8 8 0 0 1-4.3 3.6zm1.7-5.6a16 16 0 0 0 0-4h3.4a8 8 0 0 1 0 4z"/></svg>
        www.northbayfiberglass.com
      </li>
    </ul>

    <svg class="band" width="680" height="20" viewBox="0 0 680 20" aria-hidden="true">
      <polygon points="0,11 382,11 375,20 0,20" fill="var(--navy)"/>
      <polygon points="378,20 392,2 680,2 680,20" fill="var(--red)"/>
    </svg>
  </section>
</main>
</body>
</html>
```